Larkspur Ridge Management - Business Cards

I need business cards. My current logo was designed by a designer at this site and I very much like and am happy with the results. I would like a business card that is trendy, unique, current yet professional. I deal with high net worth clients daily

Target Market(s)

Out of state investors looking to get into the rental market in Ohio

Industry/Entity Type

Property Management, Consulting

Contact Information for Business Card

Name, Title (Chief Financial Officer) office phone number (555) 817-3094 website address larkridgemgmt.example

Font styles to use
Sans Serif

Colors
0054AA
0677BA
7BADD7
CADEEF
E8F1F8
0094D4
00A9DD
6FCCEA
C7EBF8
E9F6FB
00AB8E
00BBA5
67D7C9
C6EFE9
E9F9F6

```html
<!DOCTYPE html>
<html lang="en">
<head>
<meta charset="utf-8">
<title>Larkspur Ridge Management – Business Cards</title>
<link rel="stylesheet" href="https://fonts.googleapis.com/css2?family=Montserrat:wght@400;500;700;800&display=swap">
<style>
  :root {
    --brand-blue: #0054AA;
    --brand-blue-mid: #0677BA;
    --brand-teal: #00AB8E;
    --brand-teal-light: #67D7C9;
    --card: #ffffff;
    --ink: #2b2f36;
    --backdrop: #dcdedf;
  }
  * { box-sizing: border-box; margin: 0; padding: 0; }
  html, body {
    width: 1200px;
    height: 801px;
    overflow: hidden;
  }
  body {
    background: var(--backdrop);
    font-family: "Montserrat", sans-serif;
    position: relative;
  }
  .card {
    position: absolute;
    top: 250px;
    width: 525px;
    height: 300px;
    background: var(--card);
    border-bottom: 3px solid var(--brand-teal);
    border-right: 3px solid var(--brand-teal);
    box-shadow: 0 12px 28px rgba(0,0,0,0.18);
  }
  .card--front { left: 45px; }
  .card--back { left: 630px; }

  .wordmark {
    font-family: "Montserrat", sans-serif;
    font-weight: 800;
    color: var(--brand-blue);
    text-transform: uppercase;
    text-align: center;
    line-height: 1.15;
    letter-spacing: 0.02em;
  }
  .card--front .wordmark {
    position: absolute;
    top: 48px;
    left: 0;
    right: 0;
    font-size: 19px;
  }
  .card--back .wordmark {
    position: absolute;
    top: 50%;
    left: 60px;
    right: 60px;
    transform: translateY(-50%);
    font-size: 34px;
  }

  .details {
    position: absolute;
    top: 170px;
    left: 0;
    right: 0;
    display: flex;
    justify-content: center;
    align-items: center;
    gap: 22px;
  }
  .person { text-align: right; }
  .person__name {
    font-weight: 800;
    font-size: 22px;
    color: var(--brand-blue);
    letter-spacing: 0.04em;
  }
  .person__title {
    font-weight: 400;
    font-size: 14px;
    color: var(--ink);
    margin-top: 4px;
  }
  .divider {
    width: 1.5px;
    height: 64px;
    background: var(--brand-blue-mid);
  }
  .contact { list-style: none; }
  .contact__item {
    display: flex;
    align-items: center;
    gap: 8px;
    font-size: 14px;
    color: var(--ink);
    line-height: 1.7;
  }
  .contact__icon { width: 13px; height: 13px; fill: var(--brand-teal); flex: none; }
</style>
</head>
<body>
  <section class="card card--front" aria-label="Business card front">
    <div class="wordmark">Larkspur Ridge Management</div>
    <div class="details">
      <div class="person">
        <p class="person__name">NAME</p>
        <p class="person__title">Chief Financial Officer</p>
      </div>
      <div class="divider"></div>
      <ul class="contact">
        <li class="contact__item">
          <svg class="contact__icon" viewBox="0 0 16 16" aria-hidden="true"><path d="M3 1h3l1.5 4-2 1.3a9 9 0 0 0 4.2 4.2L11 8.5l4 1.5v3a2 2 0 0 1-2 2A12 12 0 0 1 1 3a2 2 0 0 1 2-2z"/></svg>
          (555) 817-3094
        </li>
        <li class="contact__item">
          <svg class="contact__icon" viewBox="0 0 16 16" aria-hidden="true"><path d="M1 3h14v10H1z M2.2 4l5.8 4.6L13.8 4z" fill-rule="evenodd"/></svg>
          larkridgemgmt.example
        </li>
      </ul>
    </div>
  </section>

  <section class="card card--back" aria-label="Business card back">
    <div class="wordmark">Larkspur Ridge Management</div>
  </section>
</body>
</html>
```